"Built on the grind" fitness and nutrition website/blog/forum

We need a website design for a gym training/nutrition website/blog. It is going to eventually have articles aimed at both men and women and will have content about exercise, nutrition, and the science behind both.

I want to have:
a home page
a page for all articles/blog posts about Nutrition
a page for all articles/blog posts about Training
a page where we can share articles about workouts targeting different muscle groups
a forum, where people can discuss nutrition and training (I would want this to be fairly simple to use and control as I am not a coder/programmer)

Design wise, I would like to use high contrast colours, such as black and white, but definitely open to some sort of colour theme, maybe some blue, or red, or purple, I am not sure, I would have to see an example.

We will be monetising this site with adverts, so there needs to be some space built in for this in the theme, however we don't want this to be overbearing, I don't want this to look like a spam site.

We have a logo, I have attached this. I haven't written any content for the homepage yet, as I wanted the design first before I worked out what to write and where to put it.

We will have social media accounts on instagram, twitter and facebook so would like buttons on the header and footer for these.

Target Market(s)

Fitness enthusiasts

Industry/Entity Type

fitness

Coding

Coded - Design and coding required

Number of Pages Required

5+ page

Font styles to use
Serif
Sans Serif

Colors

Designer to choose colors to be used in the design.

Requirements
Must have
• Space for some ads, a forum area, a page for nutrition blog posts, a page for training posts, a page for workout posts.

```html
<!DOCTYPE html>
<html lang="en">
<head>
<meta charset="utf-8">
<title>Built on the grind</title>
<link rel="stylesheet" href="https://fonts.googleapis.com/css2?family=Orbitron:wght@700;800;900&family=Roboto:wght@400;500;700&display=swap">
<style>
:root{
  --red:#e3141b;
  --black:#0b0b0c;
  --dark:#16181b;
  --ink:#1b1b1b;
  --text:#333;
  --muted:#9a9a9a;
  --line:#e4e4e4;
  --white:#fff;
  --display:"Orbitron",sans-serif;
  --body:"Roboto",sans-serif;
}
*{box-sizing:border-box;margin:0;padding:0}
html,body{width:1200px;height:4640px;overflow:hidden}
body{position:relative;background:var(--white);font-family:var(--body);color:var(--text)}
.abs{position:absolute}
.photo{display:block}

/* header */
.site-header{left:0;top:0;width:1200px;height:108px;background:var(--white);z-index:3}
.brand{left:150px;top:18px;display:flex;align-items:center;gap:10px;font-family:var(--display);font-weight:800;font-size:15px;color:var(--ink);text-transform:uppercase;line-height:1.2;width:160px}
.brand-dot{width:16px;height:16px;border-radius:50%;background:var(--red);flex:none}
.follow{right:152px;top:22px;display:flex;align-items:center;gap:10px;font-family:var(--display);font-weight:800;font-size:12px;letter-spacing:2px;text-transform:uppercase;color:var(--ink)}
.social{display:flex;gap:10px}
.social span{width:30px;height:30px;border-radius:50%;background:var(--red);display:block}
.main-nav{left:320px;top:70px;display:flex;gap:52px;font-family:var(--display);font-weight:800;font-size:13px;letter-spacing:2px;text-transform:uppercase;color:var(--ink)}
.main-nav .active{color:var(--red)}

/* hero */
.hero{left:0;top:108px;width:1200px;height:540px;background:radial-gradient(ellipse at 55% 30%,#5a5f66 0%,#2a2e33 45%,#121417 100%)}
.header-notch{left:0;top:106px;z-index:2}
.hero-title{left:0;width:1200px;top:190px;text-align:center;color:var(--white)}
.hero-title .small{display:block;font-family:var(--display);font-weight:900;font-size:44px;letter-spacing:8px;text-transform:uppercase}
.hero-title .big{display:block;font-family:var(--display);font-weight:900;font-size:86px;letter-spacing:6px;text-transform:uppercase;line-height:1.05}
.btn{display:flex;align-items:center;justify-content:center;background:var(--red);color:var(--white);font-family:var(--display);font-weight:900;font-size:16px;letter-spacing:2px;text-transform:uppercase;border-radius:24px}
.hero .btn{position:absolute;left:480px;top:348px;width:240px;height:46px}

/* promo banner */
.promo{left:148px;top:686px;width:900px;height:203px;overflow:hidden}
.promo-text{position:absolute;left:300px;top:0;width:300px;height:203px;display:flex;align-items:center;justify-content:center;text-align:center;color:var(--white);font-family:var(--display);font-weight:900;font-size:21px;letter-spacing:2px;line-height:1.45;text-transform:uppercase}

/* headings */
.section-title{font-family:var(--display);font-weight:900;font-size:28px;letter-spacing:3px;text-transform:uppercase;color:var(--ink)}

/* cards */
.card{background:var(--white);border:1px solid var(--line);width:302px}
.card .photo{width:100%;height:165px}
.card-body{padding:20px 22px 18px}
.card-title{font-family:var(--display);font-weight:800;font-size:13.5px;letter-spacing:1.5px;line-height:1.35;text-transform:uppercase;color:var(--ink)}
.author{display:flex;align-items:center;gap:6px;margin-top:10px;color:var(--red);font-size:12px;font-weight:700}
.excerpt{margin-top:12px;font-size:11.5px;line-height:1.5;color:var(--text)}
.meta{display:flex;gap:20px;margin-top:22px;font-size:10px;color:var(--muted)}
.meta span{display:flex;align-items:center;gap:4px}
.meta i{display:block;width:8px;height:8px;border-radius:50%;background:var(--muted)}

.side-ad{left:804px;top:1010px;width:244px;height:338px;background:linear-gradient(180deg,#6d737a 0%,#3c4147 55%,#1f2327 100%)}
.side-ad-text{position:absolute;left:0;right:0;bottom:22px;text-align:center;color:var(--white);font-family:var(--display);font-weight:900;font-size:22px;letter-spacing:2px;line-height:1.3;text-transform:uppercase}
.ad-label{left:804px;top:1560px;width:244px;text-align:center;font-size:10px;letter-spacing:1.5px;color:var(--muted);text-transform:uppercase}

/* training */
.training{left:0;top:1882px;width:1200px;height:670px;background:linear-gradient(180deg,#2b2e32 0%,#1c1e21 60%,#141518 100%)}
.training .section-title{position:absolute;left:150px;top:80px;color:var(--white)}
.feature{left:150px;top:140px;width:489px;height:440px;background:var(--white)}
.feature .photo{width:100%;height:228px}
.feature .card-body{padding:24px 22px}
.feature .card-title{font-size:14.5px}
.play{position:absolute;left:50%;top:50%;transform:translate(-50%,-50%)}
.mini-list{left:664px;top:143px;width:388px;display:flex;flex-direction:column;gap:15px}
.mini{position:relative;height:135px;background:var(--white);display:flex;gap:12px;padding:6px}
.mini .photo{width:146px;height:123px;flex:none;position:relative}
.mini-body{padding-top:22px;padding-right:10px}
.mini-body .card-title{font-size:12.5px}
.mini-body .excerpt{margin-top:8px;font-size:11px}
.mini-body .meta{margin-top:12px}
.mini.is-active{background:var(--red)}
.mini.is-active .card-title,.mini.is-active .excerpt,.mini.is-active .meta{color:var(--white)}
.mini.is-active .meta i{background:var(--white)}

/* workouts */
.workouts-title{left:0;width:1200px;top:2628px;text-align:center}
.workout-row{left:128px;top:2702px;display:flex;gap:18px}

/* banner 2 */
.promo2{left:148px;top:3167px;width:900px;height:203px;background:var(--black);overflow:hidden}
.promo2-text{position:absolute;left:600px;top:0;width:300px;height:203px;display:flex;flex-direction:column;align-items:center;justify-content:center;text-align:center;color:var(--white);font-family:var(--display);font-weight:900;font-size:19px;letter-spacing:2px;line-height:1.3;text-transform:uppercase}
.promo2-text .cta{margin-top:12px;color:var(--red);font-size:15px}

/* forum */
.forum-title{left:0;width:1200px;top:3434px;text-align:center}
.forum{left:196px;top:3522px;width:820px}
.topic{display:flex;align-items:center;height:144px}
.avatar{width:82px;height:82px;border-radius:50%;background:linear-gradient(180deg,#d9c7b8,#a98f7c);flex:none}
.topic-main{width:430px;margin-left:18px}
.topic-main h3{font-size:13.5px;font-weight:500;color:var(--ink);line-height:1.3}
.topic-main p{margin-top:8px;font-size:10px;line-height:1.45;color:var(--muted)}
.stats{margin-left:50px;border-left:1px solid var(--line);height:64px;display:flex;align-items:center;gap:46px;padding-left:38px}
.stat{text-align:center;font-size:10px;color:var(--muted)}
.stat b{display:block;font-size:13px;font-weight:500;color:#666}
.load-more{left:480px;top:4107px;width:240px;height:46px}

/* footer */
.footer-band{left:0;top:4240px}
.site-footer{left:0;top:4300px;width:1200px;height:340px;background:linear-gradient(90deg,#1a1c1f 0%,#25282c 60%,#1d1f22 100%)}
.footer-brand{left:165px;top:120px;display:flex;align-items:center;gap:10px;font-family:var(--display);font-weight:800;font-size:18px;color:var(--white);text-transform:uppercase;line-height:1.25;width:170px}
.footer-col{top:62px;color:var(--white)}
.footer-col h4{font-family:var(--display);font-weight:900;font-size:14px;letter-spacing:2px;text-transform:uppercase;margin-bottom:26px}
.links li{list-style:none;font-size:14px;margin-bottom:14px}
.contact li{list-style:none;display:flex;align-items:center;gap:12px;font-size:14px;margin-bottom:14px;line-height:1.25}
.contact .ico{width:32px;height:32px;border-radius:50%;background:var(--red);display:flex;align-items:center;justify-content:center;flex:none}
.email-field{width:228px;height:40px;border:1.5px solid var(--white);border-radius:20px;color:var(--white);font-size:11px;display:flex;align-items:center;padding-left:18px}
.footer-col .btn{width:118px;height:30px;margin-top:10px;font-size:13px;border-radius:16px}
.copyright{left:150px;top:292px;color:var(--white);font-size:12.5px}
.footer-social{left:928px;top:284px}
.footer-social span{width:28px;height:28px}
</style>
</head>
<body>

<header class="site-header abs">
  <div class="brand abs"><span class="brand-dot"></span>Built on the grind</div>
  <div class="follow abs">Follow us
    <div class="social" aria-label="Social media links"><span aria-label="Social profile"></span><span aria-label="Social profile"></span><span aria-label="Social profile"></span></div>
  </div>
  <nav class="main-nav abs">
    <span class="active">Home</span><span>Nutrition</span><span>Articles</span><span>Training</span><span>Workouts</span>
  </nav>
</header>

<section class="hero abs" role="img" aria-label="Athlete training in a dark gym">
  <h1 class="hero-title abs"><span class="small">Built on the</span><span class="big">Grind</span></h1>
  <a class="btn">View more</a>
</section>
<svg class="header-notch abs" width="330" height="22" viewBox="0 0 330 22"><polygon points="0,0 330,0 300,22 0,22" fill="#fff"/></svg>

<section class="promo abs">
  <div class="photo abs" style="left:0;top:0;width:330px;height:203px;background:linear-gradient(135deg,#c9cdd2,#7d848c)" role="img" aria-label="Woman training with weights in a gym"></div>
  <div class="photo abs" style="left:570px;top:0;width:330px;height:203px;background:linear-gradient(135deg,#b8c2cc,#6f7882)" role="img" aria-label="Older adults lifting kettlebells"></div>
  <svg class="abs" style="left:0;top:0" width="900" height="203"><polygon points="280,0 650,0 560,203 250,203" fill="#e3141b"/></svg>
  <div class="promo-text">Lorem ipsum<br>dolor amet<br>onsectet</div>
</section>

<h2 class="section-title abs" style="left:150px;top:950px">Nutritional posts</h2>

<article class="card abs" style="left:150px;top:1012px">
  <div class="photo" style="background:linear-gradient(135deg,#6b7a4c,#2c2f2a)" role="img" aria-label="Bowl of salad with avocado"></div>
  <div class="card-body"><h3 class="card-title">Lorem ipsum dolor sitlore magna</h3>
    <div class="author"><svg width="10" height="11"><circle cx="5" cy="3" r="3" fill="#e3141b"/><path d="M0 11a5 5 0 0 1 10 0z" fill="#e3141b"/></svg>By Rennick</div>
    <p class="excerpt">Lorem ipsum dolor sit amet, cleoonsea dipiscing do eiusmod tempor incididunt ut labore ets magna aliquacomm.</p>
    <div class="meta"><span><i></i>11 min read</span><span><i></i>88K</span><span><i></i>Dec 26, 2022</span></div></div>
</article>
<article class="card abs" style="left:469px;top:1012px">
  <div class="photo" style="background:linear-gradient(135deg,#e9e9e6,#b9b6ae)" role="img" aria-label="Man drinking a protein shake in a kitchen"></div>
  <div class="card-body"><h3 class="card-title">Lorem ipsum dolor sitlore magna</h3>
    <div class="author"><svg width="10" height="11"><circle cx="5" cy="3" r="3" fill="#e3141b"/><path d="M0 11a5 5 0 0 1 10 0z" fill="#e3141b"/></svg>By Rennick</div>
    <p class="excerpt">Lorem ipsum dolor sit amet, cleoonsea dipiscing do eiusmod tempor incididunt ut labore ets magna aliquacomm.</p>
    <div class="meta"><span><i></i>11 min read</span><span><i></i>88K</span><span><i></i>Dec 26, 2022</span></div></div>
</article>
<article class="card abs" style="left:150px;top:1416px">
  <div class="photo" style="background:linear-gradient(135deg,#d8d4cc,#3a2e22)" role="img" aria-label="Woman holding a supplement tub"></div>
  <div class="card-body"><h3 class="card-title">Lorem ipsum dolor sitlore magna</h3>
    <div class="author"><svg width="10" height="11"><circle cx="5" cy="3" r="3" fill="#e3141b"/><path d="M0 11a5 5 0 0 1 10 0z" fill="#e3141b"/></svg>By Rennick</div>
    <p class="excerpt">Lorem ipsum dolor sit amet, cleoonsea dipiscing do eiusmod tempor incididunt ut labore ets magna aliquacomm.</p>
    <div class="meta"><span><i></i>11 min read</span><span><i></i>88K</span><span><i></i>Dec 26, 2022</span></div></div>
</article>
<article class="card abs" style="left:469px;top:1416px">
  <div class="photo" style="background:linear-gradient(135deg,#4a5057,#15171a)" role="img" aria-label="Hand scooping protein powder from a tub"></div>
  <div class="card-body"><h3 class="card-title">Lorem ipsum dolor sitlore magna</h3>
    <div class="author"><svg width="10" height="11"><circle cx="5" cy="3" r="3" fill="#e3141b"/><path d="M0 11a5 5 0 0 1 10 0z" fill="#e3141b"/></svg>By Rennick</div>
    <p class="excerpt">Lorem ipsum dolor sit amet, cleoonsea dipiscing do eiusmod tempor incididunt ut labore ets magna aliquacomm.</p>
    <div class="meta"><span><i></i>11 min read</span><span><i></i>88K</span><span><i></i>Dec 26, 2022</span></div></div>
</article>

<aside class="side-ad abs" role="img" aria-label="Advert: group doing push-ups in a gym class">
  <div class="side-ad-text">Lorem ip<br>loresum<br>dolor</div>
</aside>
<div class="ad-label abs">Advertisement</div>

<section class="training abs">
  <h2 class="section-title">Training posts</h2>
  <article class="feature abs">
    <div class="photo" style="position:relative;background:linear-gradient(135deg,#6a6e72,#202326)" role="img" aria-label="Man doing a plank in a gym">
      <svg class="play" width="40" height="46"><polygon points="2,2 38,23 2,44" fill="#fff"/></svg>
    </div>
    <div class="card-body"><h3 class="card-title">Lorem ipsum dolor sit et onsec tetur adipiscing elitsed do</h3>
      <div class="author"><svg width="10" height="11"><circle cx="5" cy="3" r="3" fill="#e3141b"/><path d="M0 11a5 5 0 0 1 10 0z" fill="#e3141b"/></svg>By Rennick</div>
      <p class="excerpt">Lorem ipsum dolor sit amet, cleoonsea dipiscing do eiusmod tempor incididunt ut labore ets magna aliquacomm.</p>
      <div class="meta"><span><i></i>11 min read</span><span><i></i>88K</span><span><i></i>Dec 26, 2022</span></div></div>
  </article>
  <div class="mini-list abs">
    <article class="mini">
      <div class="photo" style="background:linear-gradient(135deg,#8a7f72,#3b3530)" role="img" aria-label="Trainer coaching a client on a bench"></div>
      <div class="mini-body"><h3 class="card-title">Lorem ipsum dol</h3><p class="excerpt">Lorem ipsum dolor sit amecloeons ea dipiscing do eiusmod.</p><div class="meta"><span><i></i>11 min read</span><span><i></i>Dec 26, 2022</span></div></div>
    </article>
    <article class="mini is-active">
      <div class="photo" style="background:linear-gradient(135deg,#8a7f72,#3b3530)" role="img" aria-label="Two people training on the gym floor">
        <svg class="play" width="22" height="26"><polygon points="1,1 21,13 1,25" fill="#fff"/></svg></div>
      <div class="mini-body"><h3 class="card-title">Lorem ipsum dol</h3><p class="excerpt">Lorem ipsum dolor sit amecloeons ea dipiscing do eiusmod.</p><div class="meta"><span><i></i>11 min read</span><span><i></i>Dec 26, 2022</span></div></div>
    </article>
    <article class="mini">
      <div class="photo" style="background:linear-gradient(135deg,#5f7480,#2a3036)" role="img" aria-label="Pair lifting kettlebells">
        <svg class="play" width="22" height="26"><polygon points="1,1 21,13 1,25" fill="#fff"/></svg></div>
      <div class="mini-body"><h3 class="card-title">Lorem ipsum dol</h3><p class="excerpt">Lorem ipsum dolor sit amecloeons ea dipiscing do eiusmod.</p><div class="meta"><span><i></i>11 min read</span><span><i></i>Dec 26, 2022</span></div></div>
    </article>
  </div>
</section>

<h2 class="section-title workouts-title abs">Workouts posts</h2>
<div class="workout-row abs">
  <article class="card">
    <div class="photo" style="background:linear-gradient(135deg,#4d4a47,#121212)" role="img" aria-label="Athlete slamming a sandbag"></div>
    <div class="card-body"><h3 class="card-title">Lorem ipsum dolor sitlore magna</h3>
      <div class="author"><svg width="10" height="11"><circle cx="5" cy="3" r="3" fill="#e3141b"/><path d="M0 11a5 5 0 0 1 10 0z" fill="#e3141b"/></svg>By Rennick</div>
      <p class="excerpt">Lorem ipsum dolor sit amet, cleoonsea dipiscing do eiusmod tempor incididunt ut labore ets magna aliquacomm.</p>
      <div class="meta"><span><i></i>11 min read</span><span><i></i>88K</span><span><i></i>Dec 26, 2022</span></div></div>
  </article>
  <article class="card">
    <div class="photo" style="background:linear-gradient(135deg,#3e444a,#111315)" role="img" aria-label="Man bench pressing a barbell"></div>
    <div class="card-body"><h3 class="card-title">Lorem ipsum dolor sitlore magna</h3>
      <div class="author"><svg width="10" height="11"><circle cx="5" cy="3" r="3" fill="#e3141b"/><path d="M0 11a5 5 0 0 1 10 0z" fill="#e3141b"/></svg>By Rennick</div>
      <p class="excerpt">Lorem ipsum dolor sit amet, cleoonsea dipiscing do eiusmod tempor incididunt ut labore ets magna aliquacomm.</p>
      <div class="meta"><span><i></i>11 min read</span><span><i></i>88K</span><span><i></i>Dec 26, 2022</span></div></div>
  </article>
  <article class="card">
    <div class="photo" style="background:linear-gradient(135deg,#6b5d62,#a3343a)" role="img" aria-label="Woman lunging with dumbbells in a gym"></div>
    <div class="card-body"><h3 class="card-title">Lorem ipsum dolor sitlore magna</h3>
      <div class="author"><svg width="10" height="11"><circle cx="5" cy="3" r="3" fill="#e3141b"/><path d="M0 11a5 5 0 0 1 10 0z" fill="#e3141b"/></svg>By Rennick</div>
      <p class="excerpt">Lorem ipsum dolor sit amet, cleoonsea dipiscing do eiusmod tempor incididunt ut labore ets magna aliquacomm.</p>
      <div class="meta"><span><i></i>11 min read</span><span><i></i>88K</span><span><i></i>Dec 26, 2022</span></div></div>
  </article>
</div>

<section class="promo2 abs">
  <div class="photo abs" style="left:0;top:0;width:640px;height:203px;background:linear-gradient(135deg,#9aa1a8,#3c5466)" role="img" aria-label="Couple doing a workout on the floor"></div>
  <svg class="abs" style="left:0;top:0" width="900" height="203"><polygon points="600,0 660,0 640,203 560,203" fill="#0b0b0c"/></svg>
  <div class="promo2-text">Lorem ipsum<br>lordolor sit<br>ameonsec<br>elit sed do<span class="cta">Click here</span></div>
</section>

<h2 class="section-title forum-title abs">Our forum</h2>
<div class="forum abs">
  <div class="topic"><div class="avatar" role="img" aria-label="Member profile photo"></div>
    <div class="topic-main"><h3>Lorem ipsum dolor sit amet, consectetur adipiscing elit, sed do eiusmod tempor incididunt ut labore et dolore magna?</h3><p>Lorem ipsum dolor sit amet, consectetur adipiscing elit, sed do eiusmod tempor incididunt ut labore et dolore magna aliqua. Quis ipsum suspendisse</p></div>
    <div class="stats"><div class="stat"><b>985</b>Likes</div><div class="stat"><b>432</b>Comments</div><div class="stat"><b>15</b>Shares</div></div></div>
  <div class="topic"><div class="avatar" role="img" aria-label="Member profile photo"></div>
    <div class="topic-main"><h3>Lorem ipsum dolor sit amet, consectetur adipiscing elit, sed do eiusmod tempor incididunt ut labore et dolore magna?</h3><p>Lorem ipsum dolor sit amet, consectetur adipiscing elit, sed do eiusmod tempor incididunt ut labore et dolore magna aliqua. Quis ipsum suspendisse</p></div>
    <div class="stats"><div class="stat"><b>985</b>Likes</div><div class="stat"><b>432</b>Comments</div><div class="stat"><b>15</b>Shares</div></div></div>
  <div class="topic"><div class="avatar" role="img" aria-label="Member profile photo"></div>
    <div class="topic-main"><h3>Lorem ipsum dolor sit amet, consectetur adipiscing elit, sed do eiusmod tempor incididunt ut labore et dolore magna?</h3><p>Lorem ipsum dolor sit amet, consectetur adipiscing elit, sed do eiusmod tempor incididunt ut labore et dolore magna aliqua. Quis ipsum suspendisse</p></div>
    <div class="stats"><div class="stat"><b>985</b>Likes</div><div class="stat"><b>432</b>Comments</div><div class="stat"><b>15</b>Shares</div></div></div>
  <div class="topic"><div class="avatar" role="img" aria-label="Member profile photo"></div>
    <div class="topic-main"><h3>Lorem ipsum dolor sit amet, consectetur adipiscing elit, sed do eiusmod tempor incididunt ut labore et dolore magna?</h3><p>Lorem ipsum dolor sit amet, consectetur adipiscing elit, sed do eiusmod tempor incididunt ut labore et dolore magna aliqua. Quis ipsum suspendisse</p></div>
    <div class="stats"><div class="stat"><b>985</b>Likes</div><div class="stat"><b>432</b>Comments</div><div class="stat"><b>15</b>Shares</div></div></div>
</div>
<a class="btn load-more abs">Load more here</a>

<svg class="footer-band abs" width="1200" height="80" viewBox="0 0 1200 80"><polygon points="0,0 1200,38 1200,60 0,60" fill="#e3141b"/><polygon points="0,60 0,30 1200,52 1200,60" fill="#1a1c1f"/></svg>
<footer class="site-footer abs">
  <div class="footer-brand abs"><span class="brand-dot"></span>Built on the grind</div>
  <div class="footer-col abs" style="left:384px"><h4>Links</h4>
    <ul class="links"><li>Our Forum</li><li>Nutrition Posts</li><li>Training Posts</li><li>Workout Posts</li></ul></div>
  <div class="footer-col abs" style="left:565px"><h4>Contact us</h4>
    <ul class="contact">
      <li><span class="ico"><svg width="12" height="16"><path d="M6 0a6 6 0 0 1 6 6c0 4-6 10-6 10S0 10 0 6a6 6 0 0 1 6-6z" fill="#fff"/><circle cx="6" cy="6" r="2.2" fill="#e3141b"/></svg></span>123 ipsum dolor sit<br>consectetur adip</li>
      <li><span class="ico"><svg width="16" height="12"><rect width="16" height="12" rx="1" fill="#fff"/><path d="M0 1l8 6 8-6" stroke="#e3141b" stroke-width="1.5" fill="none"/></svg></span>hello@builtonthegrind.net</li>
      <li><span class="ico"><svg width="14" height="14"><path d="M3 0l3 3-2 2c1 2 3 4 5 5l2-2 3 3-2 3C6 14 0 8 0 3z" fill="#fff"/></svg></span>888 888 8888</li>
    </ul></div>
  <div class="footer-col abs" style="left:820px"><h4>Newsletter</h4>
    <div class="email-field">Enter Email Here......</div>
    <a class="btn">Submit</a></div>
  <p class="copyright abs">Copyright © 2023 Built on the grind All Rights Reserved</p>
  <div class="social footer-social abs" aria-label="Social media links"><span aria-label="Social profile"></span><span aria-label="Social profile"></span><span aria-label="Social profile"></span></div>
</footer>

</body>
</html>
```